Land Buying Company Needs Letterhead for Direct Mail Marketing to Land Owners

We are looking for a professional letterhead that we will be including in our direct mail marketing. We will be sending this to land owners who may be interested in selling or purchasing land.

The letterhead needs to be editable. Headers and footers would look nice, but we are open. We would want it to include our address, website, phone, and email info. For right now the address to use for design purposes would the following:

Address: 415 Bramwell Avenue #600
Dallas, TX 75219
Website - www.quillridgeacres.example
Email - info@quillridgeacres.example
Phone - 866-402-ACRE

I have attached our logo zip file that we just had done on Pixel Guild. Let me know what questions you have, and thank you.

```html
<!DOCTYPE html>
<html lang="en">
<head>
<meta charset="utf-8">
<title>Quill Ridge Acres Letterhead</title>
<link rel="stylesheet" href="https://fonts.googleapis.com/css2?family=Arimo:wght@400;700&display=swap">
<style>
  :root {
    --brand-green: #4a6a2b;
    --ink-black: #050505;
    --paper: #ffffff;
    --text-light: #ffffff;
  }
  * { margin: 0; padding: 0; box-sizing: border-box; }
  html, body {
    width: 849px;
    height: 1200px;
    overflow: hidden;
    background: var(--paper);
  }
  .letterhead {
    position: relative;
    width: 849px;
    height: 1200px;
    background: var(--paper);
    font-family: "Arimo", Arial, sans-serif;
  }
  .header {
    position: absolute;
    top: 0;
    left: 0;
    width: 849px;
    height: 184px;
    display: flex;
  }
  .header__brand {
    width: 495px;
    height: 100%;
    background: var(--brand-green);
    display: flex;
    align-items: center;
    padding-left: 66px;
    gap: 16px;
  }
  .brand__dot {
    width: 52px;
    height: 52px;
    border-radius: 50%;
    background: var(--text-light);
    flex: none;
  }
  .brand__name {
    color: var(--text-light);
    font-weight: 700;
    font-size: 30px;
    letter-spacing: 2px;
    text-transform: uppercase;
    line-height: 1;
  }
  .header__contact {
    flex: 1;
    height: 100%;
    background: var(--ink-black);
    padding: 52px 0 0 43px;
  }
  .contact-list {
    list-style: none;
    color: var(--text-light);
    font-size: 19px;
    line-height: 23px;
  }
  .footer {
    position: absolute;
    left: 0;
    top: 1132px;
    width: 849px;
    height: 46px;
  }
  .footer svg { display: block; }
</style>
</head>
<body>
  <div class="letterhead">
    <header class="header">
      <div class="header__brand">
        <span class="brand__dot"></span>
        <span class="brand__name">Quill Ridge Acres</span>
      </div>
      <div class="header__contact">
        <ul class="contact-list">
          <li>415 Bramwell Avenue #600</li>
          <li>Dallas, TX 75219</li>
          <li>866-402-ACRE</li>
          <li>www.quillridgeacres.example</li>
          <li>info@quillridgeacres.example</li>
        </ul>
      </div>
    </header>

    <footer class="footer">
      <svg width="849" height="46" viewBox="0 0 849 46" aria-hidden="true">
        <rect class="footer__band" x="0" y="0" width="849" height="46" fill="var(--ink-black)"/>
        <polygon class="footer__divider" points="618,0 630,0 600,46 588,46" fill="var(--paper)"/>
        <polygon class="footer__accent" points="630,0 849,0 849,46 600,46" fill="var(--brand-green)"/>
      </svg>
    </footer>
  </div>
</body>
</html>
```